VARLEX CONSULTING / PROJECT MANAGEMENT WEB DESIGN

Design Brief: Varlex Consulting Website

I own 'VARLEX' business name and therefore can keep the name and logo simple i.e. VARLEX only and incorporate consulting / Project Management within the design or text.

Purpose:

The purpose of this project is to create a website for Varlex.com.au, a project management consulting company. The website will promote the company's services, allowing potential clients to learn more about Varlex and its capabilities. The website should be professional, easy to navigate, and provide all necessary information for potential clients.

Target Audience:

Clients in the Oil & Gas, LNG, and Chemical industry
Businesses and organizations in need of project management and engineering consultancy services
Potential clients looking for information about the company and its services
Key Elements:
Clean and modern design that reflects the company's professional image and incorporates the company logo

Clear and easy-to-use navigation menu

“Homepage” that promotes the company's main services and includes the company's mission statement.

Services:

PROJECT MANAGEMENT
PROJECT ENGINEERING
QUALITY MANAGEMENT AND PROCESS DEVELOPMENT
BUSINESS CASE DEVELOPMENT
ENGINEERING & DESIGN MANAGEMENT
CONCEPT STUDIES AND PROJECT SUPPORT
CONSTRUCTION MANAGEMENT
CONTRACT MANAGEMENT / CLAIMS PROCUREMENT / SUPPLY CHAIN SUPPORT
COMMERCIAL LIABILITY & RISK MANAGEMENT

Mission Statement:

"Our mission at Varlex is to provide expert project management and engineering consultancy services that help our clients achieve their goals and exceed their expectations. We will accomplish this by offering a full range of services, providing experienced and highly-qualified professionals, building strong relationships with our clients, continuously improving our services, and maintaining a reputation for excellence."

"About" page that includes client-supplied text about the company
"Contact" page with an editable form, email, and phone number for potential clients to get in touch with the company

Design Style:

Professional and modern
Clean and simple layout
Use of the company's colors and branding (subject to change)
Use of high-quality images that reflect the industry and services

Functionality:
Responsive design that is optimized for all devices and screen sizes

Website will be coded and uploaded to a content management system (CMS) for easy updates and maintenance
Website will be optimized for search engines and include all necessary SEO elements
Website will be fully tested for compatibility with all modern web browsers and devices
Website will be secured with an SSL certificate to ensure the safety of user data (client hosting includes SSL certificate).

Target Market(s)

Clients in the Oil & Gas, LNG, and Chemical industry Businesses and organizations in need of project management and engineering consultancy services Potential clients looking for information about the company and its services

Industry/Entity Type

Oil & Gas, LNG, and Chemical industry Businesses and organizations

Coding

Coded - Design and coding required

Number of Pages Required

3 page

Font styles to use
Sans Serif

Colors
0054AA
0677BA
7BADD7
CADEEF
E8F1F8
EB3D1F
EC4F4E
F09395
F8D3D4
FCEDEE
6B429C
8869AF
B7A5CE
E3DAEB
F3F0F8

Requirements
Must have
• HOME ABOUT AND CONTACT PAGE
Nice to have
• Fresh look, open to ideas
Should not have
• Stock images and hand shakes and meeting rooms..

```html
<!DOCTYPE html>
<html lang="en">
<head>
<meta charset="utf-8">
<title>Varlex Consulting</title>
<link href="https://fonts.googleapis.com/css2?family=Montserrat:wght@400;500;600;700;800;900&display=swap" rel="stylesheet">
<style>
:root{
  --sky:#2aaaf4;
  --sky-soft:#e3f3fd;
  --navy:#0c2340;
  --deep:#14549f;
  --purple:#6b429c;
  --ink:#111111;
  --grey:#5d5d5d;
  --line:#bdbdbd;
  --white:#ffffff;
}
*{box-sizing:border-box;margin:0;padding:0}
html,body{width:1200px;height:3797px;overflow:hidden}
body{position:relative;background:var(--white);font-family:"Montserrat",sans-serif;color:var(--ink)}
.abs{position:absolute}

/* header */
.hero{left:0;top:0;width:1200px;height:800px;background:linear-gradient(100deg,#1d63b4 0%,#1a4f94 35%,#0f2c52 65%,#08131f 100%)}
.header-bar{left:0;top:0;width:1200px;height:99px;background:var(--white)}
.brand-disc{left:139px;top:-88px;width:256px;height:256px;border-radius:50%;background:var(--white)}
.brand-dot{left:247px;top:10px;width:40px;height:40px;border-radius:50%;background:var(--sky)}
.brand-name{left:139px;top:93px;width:256px;text-align:center;font-weight:700;font-size:21px;color:var(--sky)}
.call{left:713px;top:13px;display:flex;align-items:center;gap:8px;font-weight:700;font-size:19px;color:var(--sky)}
.call-icon{width:31px;height:31px;border-radius:50%;background:var(--sky);display:flex;align-items:center;justify-content:center}
.nav{top:60px;font-weight:500;font-size:17px;color:var(--ink);transform:translateX(-50%)}
.search{left:1018px;top:54px;width:37px;height:37px;border-radius:50%;background:var(--purple);display:flex;align-items:center;justify-content:center}

.hero-title{left:141px;top:272px;font-weight:800;font-size:66px;line-height:70px;color:var(--white);letter-spacing:1px}
.pill{display:flex;align-items:center;justify-content:space-between;border-radius:40px;background:var(--purple);color:var(--white);font-weight:700}
.pill-dot{border-radius:50%;background:var(--white);display:flex;align-items:center;justify-content:center}
.hero-btn{left:141px;top:457px;width:194px;height:60px;padding:0 10px 0 26px;font-size:17px}
.hero-btn .pill-dot{width:34px;height:34px}
.dots span{position:absolute;left:0;width:8px;height:8px;border-radius:50%;background:var(--white)}

/* mission */
.mission-art{left:143px;top:815px;width:400px;height:420px}
.mission-title{left:594px;top:820px;font-weight:800;font-size:66px;color:var(--ink)}
.mission-sub{left:594px;top:898px;font-weight:800;font-size:40px;color:var(--sky)}
.mission-text{left:594px;top:964px;width:458px;font-size:14.5px;line-height:24.8px;color:var(--grey);text-align:justify}
.read-btn{left:594px;top:1166px;width:151px;height:49px;padding:0 7px 0 22px;font-size:13px}
.read-btn .pill-dot{width:30px;height:30px}

/* services */
.section-title{left:0;width:1200px;text-align:center;font-weight:800;font-size:64px;color:var(--ink)}
.service{width:289px;height:289px;border-radius:50%;border:2px solid var(--sky);box-shadow:2px 5px 0 var(--sky);background:var(--white);display:flex;flex-direction:column;align-items:center;padding-top:78px;text-align:center}
.service svg{width:80px;height:80px;fill:none;stroke:var(--ink);stroke-width:2.4;stroke-linecap:round;stroke-linejoin:round}
.service-name{margin-top:16px;font-weight:500;font-size:18.5px;line-height:23px;color:var(--ink);text-transform:uppercase}
.service.is-active{background:var(--sky);box-shadow:none}
.service.is-active svg{stroke:var(--white)}
.service.is-active .service-name{color:var(--white)}

/* contact */
.field{height:54px;border:1.5px solid var(--line);background:var(--white);padding:0 22px;display:flex;align-items:center;font-size:15px;color:#555}
.field.message{align-items:flex-start;padding-top:16px}
.submit-btn{left:525px;top:3173px;width:151px;height:49px;padding:0 7px 0 40px;font-size:13px}
.submit-btn .pill-dot{width:30px;height:30px}

/* footer */
.footer-head{top:3420px;font-weight:600;font-size:16px;color:var(--white)}
.footer-text{font-size:13.5px;line-height:21px;color:var(--white)}
.news-input{left:143px;top:3529px;width:275px;height:39px;border-radius:20px;background:var(--white);padding-left:16px;display:flex;align-items:center;font-size:12px;color:#777}
.subscribe{left:144px;top:3585px;width:139px;height:33px;border-radius:18px;background:var(--purple);color:var(--white);font-weight:700;font-size:14px;display:flex;align-items:center;justify-content:center}
.contact-row{left:485px;display:flex;gap:18px}
.contact-row svg{flex:none;width:20px;height:20px;fill:var(--white)}
.social{left:955px;display:flex;align-items:center;gap:10px}
.social span.ring{width:23px;height:23px;border-radius:50%;border:1.5px solid var(--white)}
.copyright{left:0;top:3744px;width:1200px;text-align:center;font-size:13px;color:var(--white)}
</style>
</head>
<body>

<!-- hero -->
<div class="abs hero" role="img" aria-label="Photo of hands typing on a laptop with a glowing project timeline chart"></div>
<svg class="abs" style="left:0;top:600px" width="1200" height="220" viewBox="0 600 1200 220">
  <path d="M0 760 C220 640 450 630 700 700 C900 760 1100 720 1200 620 L1200 820 L0 820 Z" fill="var(--white)"/>
  <path d="M0 745 C220 620 450 615 700 690 C880 740 1020 740 1110 718 C980 760 860 752 700 712 C450 650 230 660 0 800 Z" fill="var(--sky)"/>
</svg>

<header>
  <div class="abs header-bar"></div>
  <div class="abs brand-disc"></div>
  <div class="abs brand-dot"></div>
  <div class="abs brand-name">VARLEX RESOURCES</div>
  <div class="abs call">
    <span class="call-icon"><svg width="16" height="16" viewBox="0 0 24 24"><path fill="#fff" d="M6.6 10.8a15 15 0 006.6 6.6l2.2-2.2c.3-.3.7-.4 1-.2 1.1.4 2.3.6 3.6.6.6 0 1 .4 1 1V20c0 .6-.4 1-1 1A17 17 0 013 4c0-.6.4-1 1-1h3.5c.6 0 1 .4 1 1 0 1.3.2 2.5.6 3.6.1.3 0 .7-.2 1z"/></svg></span>
    CALL : +1 555 010 2030
  </div>
  <nav>
    <a class="abs nav" style="left:615px">HOME</a>
    <a class="abs nav" style="left:709px">ABOUT</a>
    <a class="abs nav" style="left:821px">SERVICES</a>
    <a class="abs nav" style="left:942px">CONTACT</a>
  </nav>
  <div class="abs search"><svg width="16" height="16" viewBox="0 0 24 24" fill="none" stroke="#fff" stroke-width="3"><circle cx="10" cy="10" r="6"/><path d="M15 15l5 5"/></svg></div>
</header>

<h1 class="abs hero-title">VARLEX<br>CONSULTING</h1>
<a class="abs pill hero-btn">GET STARTED <span class="pill-dot"><svg width="16" height="16" viewBox="0 0 24 24" fill="none" stroke="var(--sky)" stroke-width="3"><path d="M8 5l7 7-7 7"/></svg></span></a>
<div class="abs dots" style="left:1138px;top:438px">
  <span style="top:0"></span><span style="top:24px;background:var(--sky)"></span><span style="top:47px"></span>
</div>

<!-- mission -->
<svg class="abs mission-art" viewBox="0 0 400 420" role="img" aria-label="Photo of consultants at work, framed in a curved shape">
  <defs><linearGradient id="missionFill" x1="0" y1="0" x2="1" y2="1"><stop offset="0" stop-color="#3a8fd6"/><stop offset="1" stop-color="#0c3f80"/></linearGradient></defs>
  <ellipse cx="200" cy="210" rx="190" ry="200" fill="url(#missionFill)"/>
</svg>
<h2 class="abs mission-title">MISSION</h2>
<div class="abs mission-sub">VARLEX RESOURCES</div>
<p class="abs mission-text">Our mission at Varlex is to provide expert project management and engineering consultancy services that help our clients achieve their goals and exceed their expectations. We will accomplish this by offering a full range of services, providing experienced and highly-qualified professionals, building strong relationships with our clients, continuously improving our services, and maintaining a reputation for excellence.</p>
<a class="abs pill read-btn">READ MORE <span class="pill-dot"><svg width="14" height="14" viewBox="0 0 24 24" fill="none" stroke="var(--sky)" stroke-width="3"><path d="M8 5l7 7-7 7"/></svg></span></a>
<svg class="abs" style="left:0;top:1220px" width="1200" height="180" viewBox="0 1220 1200 180">
  <path d="M0 1228 C60 1330 300 1395 560 1370 C760 1350 920 1318 1052 1308 C900 1315 760 1330 560 1340 C300 1355 90 1330 0 1290 Z" fill="var(--sky)"/>
</svg>

<!-- services -->
<h2 class="abs section-title" style="top:1448px">OUR SERVICES</h2>

<div class="abs service" style="left:142px;top:1573px">
  <svg viewBox="0 0 80 80"><rect x="10" y="6" width="44" height="62"/><path d="M16 14h32M16 28h20M16 36h20M16 44h32M16 52h26"/><rect x="16" y="20" width="18" height="4"/><circle cx="60" cy="56" r="9"/><circle cx="60" cy="56" r="3"/><path d="M10 68h40"/></svg>
  <div class="service-name">Project<br>Management</div>
</div>
<div class="abs service" style="left:456px;top:1573px">
  <svg viewBox="0 0 80 80"><rect x="14" y="6" width="50" height="60"/><path d="M10 72h60M24 66v6"/><circle cx="39" cy="34" r="12"/><circle cx="39" cy="34" r="4"/><path d="M39 18v4M39 46v4M23 34h4M51 34h4"/><path d="M30 56h18"/></svg>
  <div class="service-name">Project<br>Engineering</div>
</div>
<div class="abs service" style="left:768px;top:1573px">
  <svg viewBox="0 0 80 80"><circle cx="44" cy="26" r="14"/><path d="M38 26l5 5 8-9"/><path d="M38 40l-4 12 10-5 10 5-4-12"/><path d="M8 60l12-8h16l6 4h-12M8 72l12-6h20l18-12"/></svg>
  <div class="service-name">Quality Management<br>and Process<br>Development</div>
</div>

<div class="abs service" style="left:142px;top:1897px">
  <svg viewBox="0 0 80 80"><path d="M6 66h68"/><path d="M12 66V18h30"/><rect x="20" y="44" width="6" height="20"/><rect x="30" y="36" width="6" height="28"/><rect x="40" y="50" width="6" height="14"/><circle cx="54" cy="26" r="14"/><path d="M64 36l10 10"/></svg>
  <div class="service-name">Business Case<br>Development</div>
</div>
<div class="abs service is-active" style="left:456px;top:1897px">
  <svg viewBox="0 0 80 80"><path d="M10 20h52v50H10zM10 20c-4 0-6 4-6 8v34c0 6 4 8 6 8"/><circle cx="36" cy="22" r="9"/><path d="M32 34h8M33 38h6"/><circle cx="40" cy="52" r="8"/><circle cx="40" cy="52" r="3"/><path d="M66 10v46l-3 6-3-6V10z"/></svg>
  <div class="service-name">Engineering &amp;<br>Design Management</div>
</div>
<div class="abs service" style="left:768px;top:1897px">
  <svg viewBox="0 0 80 80"><circle cx="40" cy="18" r="10"/><circle cx="40" cy="18" r="4"/><path d="M12 18h14M18 12l-6 6 6 6M54 18h14M62 12l6 6-6 6"/><path d="M40 28v14M14 42h52M14 42v12M40 42v12M66 42v12"/><circle cx="14" cy="62" r="6"/><rect x="34" y="56" width="12" height="12"/><path d="M66 56l7 12H59z"/></svg>
  <div class="service-name">Concept Studies<br>and Project<br>Support</div>
</div>

<div class="abs service" style="left:142px;top:2221px">
  <svg viewBox="0 0 80 80"><circle cx="40" cy="14" r="8"/><path d="M28 36c0-8 6-12 12-12s12 4 12 12z"/><rect x="8" y="44" width="20" height="26"/><path d="M12 52h12M12 58h12M12 64h8"/><circle cx="58" cy="56" r="12"/><circle cx="58" cy="56" r="5"/><path d="M30 56h12M36 52l-4 4 4 4"/></svg>
  <div class="service-name">Construction<br>Management</div>
</div>
<div class="abs service" style="left:456px;top:2221px">
  <svg viewBox="0 0 80 80"><path d="M16 8h44v58H16z"/><circle cx="28" cy="28" r="10"/><path d="M28 22v12M25 25h5a2 2 0 010 4h-4a2 2 0 000 4h5"/><path d="M44 22h10M44 30h10M24 46h14"/><path d="M62 32L44 58l-6 4 2-7 18-25z"/><path d="M10 66h48"/></svg>
  <div class="service-name">Contract<br>Management</div>
</div>
<div class="abs service" style="left:768px;top:2221px">
  <svg viewBox="0 0 80 80"><rect x="12" y="10" width="40" height="58"/><rect x="24" y="6" width="16" height="8"/><path d="M18 26l3 3 5-5M30 26h14M18 40l3 3 5-5M30 40h10M18 54l3 3 5-5"/><path d="M56 36l16 30H40z"/><path d="M56 46v10M56 60v1"/></svg>
  <div class="service-name">Commercial Liability<br>&amp; Risk Management</div>
</div>

<!-- contact -->
<svg class="abs" style="left:0;top:2600px" width="1200" height="130" viewBox="0 2600 1200 130">
  <path d="M72 2690 C300 2725 520 2660 760 2635 C950 2616 1100 2630 1200 2660 L1200 2710 C1080 2660 950 2650 760 2668 C520 2690 300 2720 72 2690 Z" fill="var(--sky)"/>
</svg>
<h2 class="abs section-title" style="top:2766px">CONTACT US</h2>
<form>
  <div class="abs field" style="left:233px;top:2898px;width:361px">First Name</div>
  <div class="abs field" style="left:604px;top:2898px;width:361px">Last Name</div>
  <div class="abs field" style="left:233px;top:2963px;width:361px">Email address</div>
  <div class="abs field" style="left:604px;top:2963px;width:361px">Phone Number</div>
  <div class="abs field message" style="left:233px;top:3029px;width:732px;height:115px">Message</div>
  <a class="abs pill submit-btn">SUBMIT <span class="pill-dot"><svg width="14" height="14" viewBox="0 0 24 24" fill="none" stroke="var(--sky)" stroke-width="3"><path d="M8 5l7 7-7 7"/></svg></span></a>
</form>

<!-- footer -->
<svg class="abs" style="left:0;top:3250px" width="1200" height="547" viewBox="0 3250 1200 547">
  <path d="M0 3370 C200 3290 420 3300 640 3330 C860 3360 1050 3350 1200 3300 L1200 3797 L0 3797 Z" fill="#000"/>
  <path d="M100 3285 C350 3250 560 3290 760 3325 C930 3352 1080 3345 1200 3300 L1200 3318 C1070 3370 920 3372 760 3345 C560 3310 350 3272 100 3285 Z" fill="var(--sky)"/>
</svg>
<footer>
  <div class="abs footer-head" style="left:144px">SIGN UP FOR NEWSLETTER</div>
  <p class="abs footer-text" style="left:144px;top:3469px;width:300px">excepteur sint occaecat cupidatat non proident, sunt in culpa qui officia deserunt</p>
  <div class="abs news-input">Enter email</div>
  <div class="abs subscribe">SUBSCRIBE</div>

  <div class="abs footer-head" style="left:485px">CONTACT US</div>
  <div class="abs contact-row" style="top:3475px">
    <svg viewBox="0 0 24 24"><path d="M12 2a7 7 0 00-7 7c0 5 7 13 7 13s7-8 7-13a7 7 0 00-7-7zm0 9.5A2.5 2.5 0 1112 6a2.5 2.5 0 010 5.5z"/></svg>
    <p class="footer-text">233,In egestas consectetur diam.<br>Praesent eget risus magna.<br>Vivamus vehicula</p>
  </div>
  <div class="abs contact-row" style="top:3552px">
    <svg viewBox="0 0 24 24"><path d="M6.6 10.8a15 15 0 006.6 6.6l2.2-2.2c.3-.3.7-.4 1-.2 1.1.4 2.3.6 3.6.6.6 0 1 .4 1 1V20c0 .6-.4 1-1 1A17 17 0 013 4c0-.6.4-1 1-1h3.5c.6 0 1 .4 1 1 0 1.3.2 2.5.6 3.6.1.3 0 .7-.2 1z"/></svg>
    <p class="footer-text">Phone:<br>+1 555 010 2030</p>
  </div>
  <div class="abs contact-row" style="top:3604px">
    <svg viewBox="0 0 24 24"><path d="M3 5h18v14H3z" fill="none" stroke="#fff" stroke-width="0"/><path d="M3 6h18v12H3zM3 6l9 7 9-7" /></svg>
    <p class="footer-text">Email:<br>admin@varlexmail.net</p>
  </div>

  <div class="abs footer-head" style="left:780px">QUICK LINKS</div>
  <a class="abs footer-text" style="left:783px;top:3463px">Home</a>
  <a class="abs footer-text" style="left:783px;top:3490px">About</a>
  <a class="abs footer-text" style="left:783px;top:3517px">Services</a>
  <a class="abs footer-text" style="left:783px;top:3544px">Contact</a>

  <div class="abs footer-head" style="left:955px">FOLLOW US</div>
  <a class="abs social footer-text" style="top:3467px"><span class="ring"></span>Friendbook</a>
  <a class="abs social footer-text" style="top:3501px"><span class="ring"></span>Chirpline</a>
  <a class="abs social footer-text" style="top:3535px"><span class="ring"></span>Circleplus</a>
  <a class="abs social footer-text" style="top:3568px"><span class="ring"></span>Streamtube</a>

  <p class="abs copyright">Varlex Resources © 2023 All Rights Reserved | Privacy Policy | Terms and Conditions</p>
</footer>

</body>
</html>
```